Design a colorful and bold graphic for the side of my boat

Looking for bold and/or colorful options.
Must include boat name - Keep calm cast on
Boat belongs to me and my daughter - funny, fun loving and enjoy outdoors. We use it for fishing in Texas.
We are close to the same height (she is a teenager). Like something funny/punchy/sassy. Do not want anything sexy.
Would like to end up doing a vinyl print of it to adhere to both sides of boat. Needs to be narrow and long. I will remove the wording currently on the side of the boat that says gullmark boats.

The new graphic kind of sits at two different levels. The top level and then the boat notches in about an inch down to the next one.

Hello designers! Thank you for considering my project. Im looking for a fun energy design to go on the side of my boat and feature the boat name and fish.
Name - Keep Calm Cast On. Used by - my daughter and I - both females and close to the same height. I do not want the image to be sexy in any way. Would love it to show a great image of a fish or us both catching fish. We wear ballcaps with ponytails. The image does not have to contain us but certainly can. Must have fish and boat name though. I like colorful and bold designs. No not care for childish images. I do like edgy, bold, funny, eye catching. etc. My daughter and I are both funny and fun loving and love the water and fishing. Would love to have a cool graphic that captures that spirit.
This bio is hopefully helpful. I got a number of designs previously and they did not match my requests. Thank you for your creative input and considering my project.

Colors

Designer to choose colors to be used in the design.

Requirements
Must have
• Be approx 1 foot tall and 5 feet long, show boat name, and some sort of fun image of fish/s
Nice to have
• Us represented some way - mom and daughter depicted to look like fish or both of us catching fish
Should not have
• Only words

```html
<!DOCTYPE html>
<html lang="en">
<head>
<meta charset="utf-8">
<title>Keep Calm Cast On – Boat Graphic</title>
<link rel="stylesheet" href="https://fonts.googleapis.com/css2?family=Federo&display=swap">
<style>
  :root {
    --olive-deep: #2c2f20;
    --olive-mid: #363a28;
    --olive-light: #41462f;
    --cream: #f8ecd1;
    --ring-navy: #1f3a4a;
    --badge-sun: #f1b866;
    --badge-sky: #f6dfa6;
    --badge-water: #6fa9b3;
    --badge-land: #9a6a45;
    --bass-green: #5f7a3c;
    --bass-dark: #3d5227;
  }
  html, body {
    margin: 0;
    padding: 0;
    overflow: hidden;
    background: var(--olive-deep);
  }
  .boat-graphic {
    position: relative;
    width: 1200px;
    height: 292px;
    overflow: hidden;
    background: var(--olive-deep);
  }
  .backdrop-photo {
    position: absolute;
    inset: 0;
    background:
      radial-gradient(ellipse 380px 200px at 730px 190px, var(--olive-light) 0%, transparent 70%),
      linear-gradient(100deg, var(--olive-deep) 0%, var(--olive-mid) 55%, var(--olive-deep) 100%);
  }
  .badge {
    position: absolute;
    left: 23px;
    top: 38px;
    width: 216px;
    height: 216px;
  }
  .boat-name {
    position: absolute;
    left: 0;
    top: 0;
    width: 1200px;
    height: 292px;
  }
  .boat-name text {
    font-family: "Federo", "Arial Narrow", sans-serif;
    font-weight: 400;
    font-size: 126px;
    fill: var(--cream);
    stroke: var(--cream);
    stroke-width: 7px;
    stroke-linejoin: round;
  }
</style>
</head>
<body>
<main class="boat-graphic">
  <div class="backdrop-photo" role="img" aria-label="Faint dark-olive photograph of a fishing boat riding a large ocean wave"></div>

  <svg class="badge" viewBox="0 0 216 216">
    <defs>
      <linearGradient id="badge-scene" x1="0" y1="0" x2="0" y2="1">
        <stop offset="0" stop-color="var(--badge-sky)"/>
        <stop offset="0.4" stop-color="var(--badge-sun)"/>
        <stop offset="0.62" stop-color="var(--badge-land)"/>
        <stop offset="0.68" stop-color="var(--badge-water)"/>
        <stop offset="1" stop-color="var(--badge-water)"/>
      </linearGradient>
      <radialGradient id="badge-bass" cx="0.5" cy="0.45" r="0.45">
        <stop offset="0" stop-color="var(--bass-green)" stop-opacity="0.95"/>
        <stop offset="0.6" stop-color="var(--bass-dark)" stop-opacity="0.6"/>
        <stop offset="1" stop-color="var(--bass-dark)" stop-opacity="0"/>
      </radialGradient>
    </defs>
    <circle cx="108" cy="108" r="106" fill="var(--cream)"/>
    <circle cx="108" cy="108" r="100" fill="none" stroke="var(--ring-navy)" stroke-width="3"/>
    <g role="img" aria-label="Illustration of a largemouth bass leaping from a lake at sunset with pine trees and mountains">
      <circle cx="108" cy="108" r="97" fill="url(#badge-scene)"/>
      <circle cx="108" cy="108" r="97" fill="url(#badge-bass)"/>
    </g>
  </svg>

  <svg class="boat-name" viewBox="0 0 1200 292">
    <text x="260" y="189" textLength="906" lengthAdjust="spacingAndGlyphs">KEEP CALM CAST ON</text>
  </svg>
</main>
</body>
</html>
```